Brookfarrow Osteopathy and dry needling business card

Business card for Brookfarrow Osteopathy and Dry Needling.

Industry/Entity Type

Health

Contact Information for Business Card

I do not have a phone number yet. I also do not have an email address yet. The physical address is: 48 Lower Crane Street Brookfarrow The website is: www.brookfarrowosteosteopathy.example My details are: Dr Martin Pellowe, Osteopath (B.Clin.Sci (Ost) M.Ost BSC ECON (Hons)

Colors
0094D4
00A9DD
6FCCEA
C7EBF8
E9F6FB

Requirements
Must have
• logo on the back
Nice to have
• Maybe a space for me to write an appointment time and date on the card.

```html
<!DOCTYPE html>
<html lang="en">
<head>
<meta charset="utf-8">
<title>Brookfarrow Osteopathy and Dry Needling – Business Card</title>
<link rel="stylesheet" href="https://fonts.googleapis.com/css2?family=Montserrat:wght@300;400;500;600;700&display=swap">
<style>
  :root {
    --stage: #3b3c3f;
    --brand-blue: #0094d4;
    --brand-sky: #00a9dd;
    --brand-light: #1fa8ec;
    --brand-deep: #0082c8;
    --accent-orange: #f7941d;
    --text-grey: #666666;
    --rule-grey: #9a9a9a;
    --card-white: #ffffff;
  }
  * { margin: 0; padding: 0; box-sizing: border-box; }
  html, body { width: 1200px; height: 1200px; overflow: hidden; }
  body {
    background: var(--stage);
    font-family: "Montserrat", sans-serif;
    position: relative;
  }
  .card {
    position: absolute;
    left: 165px;
    width: 908px;
    height: 519px;
    border-radius: 50px;
    overflow: hidden;
    box-shadow: 0 6px 18px rgba(0,0,0,0.25);
  }
  .card--front { top: 55px; background: var(--card-white); }
  .card--back {
    top: 615px;
    background: linear-gradient(150deg, var(--brand-sky) 0%, var(--brand-deep) 55%, var(--brand-light) 100%);
    background: linear-gradient(to top right, var(--brand-deep) 0%, #0a9fde 50%, #04b7d9 100%);
  }
  .card--back::after {
    content: "";
    position: absolute; inset: 0;
    background: radial-gradient(circle at 95% 95%, rgba(40,170,240,0.7), transparent 55%);
  }

  .brand-mark {
    position: absolute;
    display: flex; flex-direction: column; align-items: center; justify-content: center;
    text-align: center;
    font-weight: 600;
    line-height: 1.25;
    z-index: 1;
  }
  .brand-mark__dot { border-radius: 50%; margin-bottom: 10px; }
  .card--front .brand-mark { left: 73px; top: 177px; width: 170px; height: 170px; color: var(--brand-blue); font-size: 15px; }
  .card--front .brand-mark__dot { width: 22px; height: 22px; background: var(--accent-orange); }
  .card--back .brand-mark { left: 606px; top: 146px; width: 240px; height: 220px; color: #ffffff; font-size: 20px; }
  .card--back .brand-mark__dot { width: 28px; height: 28px; background: #ffffff; }

  .details { position: absolute; left: 419px; top: 85px; }
  .details__name { font-size: 35px; font-weight: 700; color: var(--brand-blue); letter-spacing: -0.2px; line-height: 1; }
  .details__role { margin-top: 10px; font-size: 17px; font-weight: 300; color: var(--accent-orange); white-space: nowrap; }
  .details__rule { margin-top: 14px; width: 39px; height: 3px; background: var(--brand-blue); }
  .contact { list-style: none; margin-top: 26px; }
  .contact__item { display: flex; align-items: center; height: 40px; font-size: 21px; color: var(--text-grey); }
  .contact__icon { width: 22px; height: 24px; margin-right: 18px; flex: none; }

  .appointment { margin-top: 44px; }
  .appointment__title { font-size: 27px; font-weight: 700; color: var(--brand-blue); line-height: 1; }
  .appointment__row { display: flex; align-items: flex-end; margin-top: 26px; font-size: 18px; font-weight: 600; color: var(--text-grey); height: 22px; }
  .appointment__row + .appointment__row { margin-top: 24px; }
  .appointment__label { width: 78px; }
  .appointment__blank { display: inline-block; width: 46px; border-bottom: 1px solid var(--rule-grey); height: 1px; margin-bottom: 3px; }
  .appointment__blank--short { width: 37px; }
  .appointment__sep { color: var(--rule-grey); font-weight: 300; margin: 0 8px; }
</style>
</head>
<body>

  <section class="card card--front" aria-label="Business card front">
    <div class="brand-mark">
      <span class="brand-mark__dot"></span>
      Brookfarrow<br>Osteopathy &amp;<br>Dry Needling
    </div>

    <div class="details">
      <h1 class="details__name">Dr Martin Pellowe,</h1>
      <p class="details__role">Osteopath (B.Clin.Sci (Ost) M.Ost BSC ECON (Hons)</p>
      <div class="details__rule"></div>

      <ul class="contact">
        <li class="contact__item">
          <svg class="contact__icon" viewBox="0 0 24 24" aria-hidden="true">
            <circle cx="12" cy="12" r="10.5" fill="none" stroke="#f7941d" stroke-width="2"/>
            <ellipse cx="12" cy="12" rx="4.5" ry="10.5" fill="none" stroke="#f7941d" stroke-width="2"/>
            <line x1="1.5" y1="12" x2="22.5" y2="12" stroke="#f7941d" stroke-width="2"/>
            <line x1="3" y1="7" x2="21" y2="7" stroke="#f7941d" stroke-width="1.6"/>
            <line x1="3" y1="17" x2="21" y2="17" stroke="#f7941d" stroke-width="1.6"/>
          </svg>
          www.brookfarrowosteosteopathy.example
        </li>
        <li class="contact__item">
          <svg class="contact__icon" viewBox="0 0 24 24" aria-hidden="true">
            <path d="M12 1.5c-5 0-9 3.9-9 8.8 0 6.3 9 12.7 9 12.7s9-6.4 9-12.7c0-4.9-4-8.8-9-8.8z" fill="#f7941d"/>
            <circle cx="12" cy="10" r="3.6" fill="none" stroke="#fff" stroke-width="2"/>
          </svg>
          48 Lower Crane Street Brookfarrow
        </li>
      </ul>

      <div class="appointment">
        <h2 class="appointment__title">Your Next Appointment</h2>
        <div class="appointment__row">
          <span class="appointment__label">Date:</span>
          <span class="appointment__blank"></span><span class="appointment__sep">/</span>
          <span class="appointment__blank"></span><span class="appointment__sep">/</span>
          <span class="appointment__blank appointment__blank--short"></span>
        </div>
        <div class="appointment__row">
          <span class="appointment__label">Time:</span>
          <span class="appointment__blank appointment__blank--short"></span><span class="appointment__sep">:</span>
          <span class="appointment__blank appointment__blank--short"></span>
        </div>
      </div>
    </div>
  </section>

  <section class="card card--back" aria-label="Business card back">
    <div class="brand-mark">
      <span class="brand-mark__dot"></span>
      Brookfarrow<br>Osteopathy &amp;<br>Dry Needling
    </div>
  </section>

</body>
</html>
```